Business card

I need a business card design for my consulting company in animal welfare for livestock. I like clean, crisp, simple.

One I imagined was double-sided:
side1: just my name and contact information
side2: silhouette of farm animals. Could be 3 (pig, cow, chicken) or all the species (pig, cow, chicken, duck, sheep, rabbit, etc) that continue the length of the card. I have attached an image of a silhouette style.

But, I am open to any concept.

Industry/Entity Type

Business

```html
<!DOCTYPE html>
<html lang="en">
<head>
<meta charset="utf-8">
<title>Helen Marsh – Business Card</title>
<link rel="stylesheet" href="https://fonts.googleapis.com/css2?family=Poppins:wght@600&family=Questrial&display=swap">
<style>
  :root {
    --backdrop: #ece8e1;
    --card-green: #33472a;
    --silhouette-green: #2b3d23;
    --name-yellow: #e3ef3a;
    --text-white: #f4f4ee;
    --card-shadow: rgba(0, 0, 0, 0.28);
  }
  * { margin: 0; padding: 0; box-sizing: border-box; }
  html, body {
    width: 1200px;
    height: 1000px;
    overflow: hidden;
    background: var(--backdrop);
  }
  .sheet {
    position: relative;
    width: 1200px;
    height: 1000px;
  }
  .card {
    position: absolute;
    left: 250px;
    width: 700px;
    height: 400px;
    background: var(--card-green);
    box-shadow: 0 6px 18px var(--card-shadow);
  }
  .card--front { top: 60px; }
  .card--back { top: 540px; }

  .animal-row {
    position: absolute;
    left: 160px;
    top: 150px;
    width: 380px;
    height: 110px;
    border-radius: 40px;
    background: linear-gradient(90deg, var(--silhouette-green), #2e4126 50%, var(--silhouette-green));
  }
  .hen-mark {
    position: absolute;
    right: 28px;
    top: 24px;
    width: 86px;
    height: 82px;
    border-radius: 40px;
    background: var(--silhouette-green);
  }

  .identity {
    position: absolute;
    left: 44px;
    top: 34px;
  }
  .identity__name {
    font-family: "Poppins", sans-serif;
    font-weight: 600;
    font-size: 23px;
    color: var(--name-yellow);
    line-height: 1.3;
  }
  .identity__role {
    font-family: "Questrial", sans-serif;
    font-size: 23px;
    color: var(--text-white);
    line-height: 1.3;
  }

  .contact {
    position: absolute;
    left: 44px;
    bottom: 28px;
    list-style: none;
    font-family: "Questrial", sans-serif;
    font-size: 23px;
    color: var(--text-white);
  }
  .contact__item {
    display: flex;
    align-items: center;
    gap: 14px;
    line-height: 1.15;
  }
  .contact__icon {
    width: 22px;
    height: 18px;
    flex: none;
  }
</style>
</head>
<body>
<main class="sheet">
  <section class="card card--front" aria-label="Card front">
    <div class="animal-row" role="img" aria-label="Faint silhouettes of a cow, a pig and a hen in a row"></div>
  </section>

  <section class="card card--back" aria-label="Card back">
    <div class="identity">
      <h1 class="identity__name">Helen Marsh</h1>
      <p class="identity__role">Welfare Services for<br>Livestock Stakeholders</p>
    </div>

    <div class="hen-mark" role="img" aria-label="Faint hen silhouette"></div>

    <ul class="contact">
      <li class="contact__item">
        <svg class="contact__icon" viewBox="0 0 22 16" aria-hidden="true">
          <rect x="1" y="1" width="20" height="14" fill="none" stroke="#f4f4ee" stroke-width="1.6"/>
          <path d="M1 1 L11 9 L21 1" fill="none" stroke="#f4f4ee" stroke-width="1.6"/>
        </svg>
        <span>helen.marsh@fieldmail.com</span>
      </li>
      <li class="contact__item">
        <svg class="contact__icon" viewBox="0 0 22 18" aria-hidden="true">
          <path d="M1 6 Q11 -2 21 6 L18 8 L15 5 Q11 3 7 5 L4 8 Z" fill="#f4f4ee"/>
          <path d="M5 9 L8 6 L14 6 L17 9 L17 17 L5 17 Z" fill="#f4f4ee"/>
          <circle cx="11" cy="12" r="2.6" fill="#33472a"/>
        </svg>
        <span>+1 555.214.3870</span>
      </li>
    </ul>
  </section>
</main>
</body>
</html>
```